Redesign of business card for Birchline Mechanical

We are looking for a new design for our business cards for Birchline Mechanical. We are a plumbing & HVAC construction company, operating on the West Coast of Canada and USA. Logo attached.
Industry/Entity Type
Construction - Plumbing & HVAC
Contact Information for Business Card
Name, address, phone numbers, email, website address
Look and feel
Each slider illustrates characteristics of the customer's brand and the style your logo design should communicate.

```html
<!DOCTYPE html>
<html lang="en">
<head>
<meta charset="utf-8">
<title>Birchline Mechanical – Business Card</title>
<link rel="stylesheet" href="https://fonts.googleapis.com/css2?family=Montserrat:wght@400;500;700&display=swap">
<style>
  :root {
    --page: #141414;
    --card: #111111;
    --card-edge: #1c1c1c;
    --ink: #ffffff;
    --band-light: #9a9a9a;
    --band-mid: #5e5e5e;
    --paper: #f4f4f4;
  }
  * { margin: 0; padding: 0; box-sizing: border-box; }
  html, body {
    width: 1200px; height: 963px; overflow: hidden;
    background: var(--page);
    font-family: "Montserrat", sans-serif;
    color: var(--ink);
  }
  .sheet {
    width: 1200px; height: 963px;
    display: flex; flex-direction: column; align-items: center; justify-content: center;
    gap: 56px;
  }
  .card {
    position: relative;
    width: 660px; height: 378px;
    background: var(--card);
    border: 1px solid var(--card-edge);
    border-radius: 22px;
    overflow: hidden;
  }
  .brand {
    display: flex; align-items: center; gap: 14px;
    font-weight: 700; text-transform: uppercase; letter-spacing: 0.06em;
    color: var(--ink);
  }
  .brand-square { background: var(--ink); flex: none; }

  /* front */
  .card-front .brand { position: absolute; left: 44px; top: 44px; font-size: 21px; }
  .card-front .brand-square { width: 20px; height: 20px; }
  .person { position: absolute; left: 44px; top: 104px; }
  .person-name { font-size: 24px; font-weight: 700; letter-spacing: 0.04em; text-transform: uppercase; }
  .person-role { font-size: 17px; font-weight: 400; margin-top: 2px; }
  .address { position: absolute; left: 44px; top: 176px; font-size: 17px; line-height: 1.3; }
  .contacts { position: absolute; left: 44px; top: 236px; list-style: none; font-size: 17px; line-height: 1.55; }
  .contacts li { display: flex; align-items: center; gap: 10px; }
  .contacts svg { width: 15px; height: 15px; flex: none; }
  .swoosh { position: absolute; inset: 0; width: 100%; height: 100%; }

  /* back */
  .card-back { display: flex; align-items: center; justify-content: center; }
  .card-back .brand { font-size: 40px; gap: 22px; }
  .card-back .brand-square { width: 38px; height: 38px; }
</style>
</head>
<body>
<main class="sheet">
  <section class="card card-front" aria-label="Card front">
    <div class="brand"><span class="brand-square"></span>Birchline Mechanical</div>
    <div class="person">
      <p class="person-name">Daniel Harper</p>
      <p class="person-role">Manager</p>
    </div>
    <p class="address">Your address, city<br>state, ZIP 0000</p>
    <ul class="contacts">
      <li>
        <svg viewBox="0 0 16 16" aria-hidden="true"><path fill="#fff" d="M3 1.5l2.5-.5 1.5 3.5-1.7 1.2a8 8 0 0 0 4 4l1.2-1.7L14 9.5l-.5 2.5c-.3 1.3-1.6 2-2.8 1.6A13 13 0 0 1 2 4.3C1.6 3.1 2 1.8 3 1.5z"/></svg>
        123-456-2100
      </li>
      <li>
        <svg viewBox="0 0 16 16" aria-hidden="true"><rect x="1" y="3" width="14" height="10" rx="1" fill="#fff"/><path d="M1.5 3.5L8 9l6.5-5.5" fill="none" stroke="#111" stroke-width="1.3"/></svg>
        youremail@mailbox.com
      </li>
      <li>
        <svg viewBox="0 0 16 16" aria-hidden="true"><circle cx="8" cy="8" r="7" fill="#fff"/><path d="M1 8h14M8 1c-3 3.5-3 10.5 0 14M8 1c3 3.5 3 10.5 0 14" fill="none" stroke="#111" stroke-width="1"/></svg>
        www.yourwebsite.com
      </li>
    </ul>
    <svg class="swoosh" viewBox="0 0 660 378" preserveAspectRatio="none" aria-hidden="true">
      <path d="M200 378 C 330 300 500 250 660 236 L660 378 Z" fill="var(--band-mid)"/>
      <path d="M230 378 C 360 312 510 262 660 250 L660 378 Z" fill="var(--band-light)"/>
      <path d="M270 378 C 400 326 530 282 660 272 L660 378 Z" fill="#0d0d0d"/>
      <path d="M290 378 C 420 334 545 292 660 282 L660 378 Z" fill="var(--paper)"/>
    </svg>
  </section>

  <section class="card card-back" aria-label="Card back">
    <div class="brand"><span class="brand-square"></span>Birchline Mechanical</div>
  </section>
</main>
</body>
</html>
```